Brivella LLC soda can design.

Welcome to Brivella luxury soda cans we offer five serious non sugar based flavors.

Soda, soda lime, soda green tea, soda tonic, soda ginger.

Plastic flag ship 750ml or 1l black label soda. Generic black label.
335 cans of same flag ship soda.

Thin tall 335 cans. Thin tall 250 cans. Normal 335 cans.

Files go to manufacturer for revision then back for final mastering.

Please center Image and scale all the same.

Pease be exact and consistent.

Transparent, white backgrounds for online selling and presentation.

Large gold font - Brivella tm
Small text - Established 2021 -
Small text with without copy.

Thank you.
Brivellallc@quorimail.com
Plaintulip@quorimail.com

Target Market(s)

Worldwide All ages generic soda

Industry/Entity Type

Soda water

Font styles to use
Serif
Decorative

Requirements
Must have
• Revisions after post manufacturer approval.
Nice to have
• 48067192 design generic soda
Should not have
• Non generic

```html
<!DOCTYPE html>
<html lang="en">
<head>
<meta charset="utf-8">
<title>Brivella Soda Can Labels</title>
<link rel="stylesheet" href="https://fonts.googleapis.com/css2?family=Bodoni+Moda:wght@500&family=Montserrat:wght@400;700&display=swap">
<style>
  :root {
    --page-bg: #ffffff;
    --band-dark: #141414;
    --band-mid: #2a2a2a;
    --gold-deep: #c79a2e;
    --gold-light: #f0d57a;
    --gold-name: #d3aa3e;
    --lime-deep: #93b52c;
    --lime-light: #dcef8a;
    --lime-name: #a9c93c;
    --blue-deep: #1558b8;
    --blue-light: #5fb4f2;
    --blue-name: #ffffff;
    --ink-dark: #151515;
    --ink-light: #ffffff;
  }
  html, body {
    margin: 0;
    padding: 0;
    width: 1200px;
    height: 900px;
    overflow: hidden;
    background: var(--page-bg);
  }
  .range {
    position: relative;
    width: 1200px;
    height: 900px;
  }
  .can-label {
    position: absolute;
    top: 174px;
    width: 204px;
    height: 516px;
    overflow: hidden;
    font-family: "Montserrat", sans-serif;
  }
  .can-label--soda { left: 184px; background: linear-gradient(90deg, var(--gold-deep) 0%, var(--gold-light) 30%, var(--gold-deep) 70%, #b88a24 100%); }
  .can-label--lime { left: 498px; background: linear-gradient(90deg, var(--lime-deep) 0%, var(--lime-light) 30%, var(--lime-deep) 70%, #86a626 100%); }
  .can-label--tonic { left: 832px; background: linear-gradient(90deg, var(--blue-deep) 0%, var(--blue-light) 30%, var(--blue-deep) 70%, #0f4aa0 100%); }

  .wave-band {
    position: absolute;
    inset: 0;
    width: 204px;
    height: 516px;
  }
  .brand-name {
    position: absolute;
    left: 0;
    right: 0;
    top: 262px;
    margin: 0;
    text-align: center;
    white-space: nowrap;
    font-family: "Bodoni Moda", serif;
    font-weight: 500;
    font-size: 34px;
    letter-spacing: -0.5px;
    line-height: 1;
  }
  .can-label--soda .brand-name { color: var(--gold-name); }
  .can-label--lime .brand-name { color: var(--lime-name); }
  .can-label--tonic .brand-name { color: var(--blue-name); }

  .established {
    position: absolute;
    left: 0;
    right: 0;
    top: 307px;
    margin: 0;
    text-align: center;
    font-size: 8.5px;
    color: var(--ink-light);
  }
  .flavour {
    position: absolute;
    left: 0;
    right: 0;
    top: 460px;
    margin: 0;
    text-align: center;
    font-size: 10.5px;
    font-weight: 700;
    letter-spacing: 0.5px;
    color: var(--ink-dark);
  }
  .volume {
    position: absolute;
    left: 0;
    right: 0;
    top: 474px;
    margin: 0;
    text-align: center;
    font-size: 11px;
    color: var(--ink-dark);
  }
  .can-label--tonic .flavour,
  .can-label--tonic .volume { color: var(--ink-light); }
</style>
</head>
<body>
<main class="range">
  <section class="can-label can-label--soda">
    <svg class="wave-band" viewBox="0 0 204 516" role="img" aria-label="Black wave band with fine flowing line pattern">
      <defs>
        <linearGradient id="band-shade" x1="0" x2="1" y1="0" y2="0">
          <stop offset="0" stop-color="#141414"/>
          <stop offset="0.35" stop-color="#2e2e2e"/>
          <stop offset="1" stop-color="#121212"/>
        </linearGradient>
      </defs>
      <path d="M0,152 C40,150 62,72 118,52 C155,40 186,44 204,48 L204,412 C172,398 134,404 104,438 C72,474 34,478 0,476 Z" fill="url(#band-shade)"/>
    </svg>
    <h2 class="brand-name">BRIVELLA</h2>
    <p class="established">Established 2021</p>
    <p class="flavour">SODA</p>
    <p class="volume">250ml</p>
  </section>

  <section class="can-label can-label--lime">
    <svg class="wave-band" viewBox="0 0 204 516" role="img" aria-label="Black wave band with fine flowing line pattern">
      <path d="M0,152 C40,150 62,72 118,52 C155,40 186,44 204,48 L204,412 C172,398 134,404 104,438 C72,474 34,478 0,476 Z" fill="url(#band-shade)"/>
    </svg>
    <h2 class="brand-name">BRIVELLA</h2>
    <p class="established">Established 2021</p>
    <p class="flavour">SODA LIME</p>
    <p class="volume">250ml</p>
  </section>

  <section class="can-label can-label--tonic">
    <svg class="wave-band" viewBox="0 0 204 516" role="img" aria-label="Black wave band with fine flowing line pattern">
      <path d="M0,152 C40,150 62,72 118,52 C155,40 186,44 204,48 L204,412 C172,398 134,404 104,438 C72,474 34,478 0,476 Z" fill="url(#band-shade)"/>
    </svg>
    <h2 class="brand-name">BRIVELLA</h2>
    <p class="established">Established 2021</p>
    <p class="flavour">SODA TONIC</p>
    <p class="volume">250ml</p>
  </section>
</main>
</body>
</html>
```